Business Card Design

I need a business card design for my law office based in Pasadena, California. I am a sole practitioner and I specialize in business transaction and litigation, probate and estate planning, taxation law, corporate and business formation, immigration and real estate. I want something that is simple, yet stands out.

A friend helped to create a logo about 6 years ago. I am open to new ideas to changing the logo.

Industry/Entity Type

Business

Contact Information for Business Card

Law Offices of Dorvan L. Mabry
842 W. Larkspur Ave., Suite 319
Pasadena, CA 90287
Tel: 626-555-0174
Fax: 626-555-0139
Email: dmabry@dlmlegalgroup.example

Attorney: Dorvan L. Mabry

```html
<!DOCTYPE html>
<html lang="en">
<head>
<meta charset="utf-8">
<title>Business Cards – Law Offices of Dorvan L. Mabry</title>
<link href="https://fonts.googleapis.com/css2?family=Cinzel:wght@500&family=Didact+Gothic&display=swap" rel="stylesheet">
<style>
  :root {
    --backdrop: #e4e5e7;
    --card: #fbfbfa;
    --ink: #1d1d1d;
    --ink-soft: #5d5d5d;
    --hatch: #e2e2e2;
    --rule: #222222;
  }
  html, body {
    margin: 0;
    width: 1200px;
    height: 800px;
    overflow: hidden;
    background: var(--backdrop);
  }
  .stage {
    position: relative;
    width: 1200px;
    height: 800px;
  }
  .card {
    position: absolute;
    width: 500px;
    height: 286px;
    background: var(--card);
    box-shadow: 0 2px 10px rgba(0,0,0,0.12);
    overflow: hidden;
  }
  .card--contact { left: 70px; top: 257px; }
  .card--brand { left: 630px; top: 257px; }

  /* contact side */
  .texture-panel {
    position: absolute;
    left: 0; top: 0;
    width: 188px; height: 100%;
    background: var(--hatch);
  }
  .accent-bar {
    position: absolute;
    left: 208px; top: 68px;
    width: 5px; height: 132px;
    background: var(--rule);
  }
  .contact-block {
    position: absolute;
    left: 224px; top: 62px;
    font-family: "Didact Gothic", sans-serif;
    color: var(--ink);
  }
  .contact-name {
    margin: 0;
    font-size: 28px;
    font-weight: 400;
    letter-spacing: 0.5px;
    line-height: 1.1;
  }
  .contact-title {
    margin: 2px 0 8px;
    font-size: 11px;
    letter-spacing: 1.5px;
    color: var(--ink-soft);
  }
  .contact-lines {
    margin: 0 0 10px;
    padding: 0;
    list-style: none;
    font-size: 11px;
    line-height: 1.45;
    color: var(--ink);
  }
  .contact-address {
    font-style: normal;
    font-size: 11px;
    line-height: 1.45;
  }
  .edge-tab {
    position: absolute;
    right: 0; top: 152px;
    width: 38px; height: 118px;
    background: var(--ink);
  }

  /* brand side */
  .band {
    position: absolute;
    left: 0; width: 100%; height: 42px;
    background: var(--hatch);
  }
  .band--top { top: 0; }
  .band--bottom { bottom: 0; }
  .brand-lockup {
    position: absolute;
    left: 0; right: 0; top: 70px;
    text-align: center;
  }
  .brand-square {
    display: inline-block;
    width: 46px; height: 46px;
    background: var(--ink);
  }
  .brand-name {
    margin: 16px 0 0;
    font-family: "Cinzel", serif;
    font-weight: 500;
    font-size: 21px;
    letter-spacing: 1px;
    color: var(--ink);
  }
</style>
</head>
<body>
<main class="stage">

  <section class="card card--contact">
    <div class="texture-panel" role="img" aria-label="Fine diagonal line texture panel"></div>
    <div class="accent-bar"></div>
    <div class="contact-block">
      <h1 class="contact-name">Dorvan L. Mabry</h1>
      <p class="contact-title">ATTORNEY</p>
      <ul class="contact-lines">
        <li>Tel: 626-555-0174</li>
        <li>Fax: 626-555-0139</li>
        <li>Email: dmabry@dlmlegalgroup.example</li>
      </ul>
      <address class="contact-address">
        842 W. Larkspur Ave., Suite 319<br>
        Pasadena, CA 90287
      </address>
    </div>
    <div class="edge-tab"></div>
  </section>

  <section class="card card--brand">
    <div class="band band--top" role="img" aria-label="Fine diagonal line texture band"></div>
    <div class="brand-lockup">
      <span class="brand-square"></span>
      <p class="brand-name">Law Offices of Dorvan L. Mabry</p>
    </div>
    <div class="band band--bottom" role="img" aria-label="Fine diagonal line texture band"></div>
  </section>

</main>
</body>
</html>
```